Stationary Package for Construction Company
Modern and Professional
Stationary Package for Construction Company - Construction
Creative Brief
Professional
Karl T. Wentworth
V.P., Operations & Sr. Project Manager
7148 Orchard Lane, Unit 512 Myrtle Beach, SC 29614
843.555.0178 ext. 214
Karl@BrimstackLLC.example
www.BrimstackLLC.example
Current logo is uploaded in .ai format. If color needs to be altered, that is ok. We may also need an alternate color for back of business card. I have also uploaded a few card samples that we already like.
Back of card should be alternate color, either red or black. Two options: One card back with logo only, and one version with logo, web address and services rendered, which I'll specify in greater detail as we narrow down specific designs that we like.

```html
<!DOCTYPE html>
<html lang="en">
<head>
<meta charset="utf-8">
<title>Brimstack Construction – Business Cards</title>
<link href="https://fonts.googleapis.com/css2?family=Oswald:wght@600&family=Open+Sans:wght@400;600&display=swap" rel="stylesheet">
<style>
  :root {
    --backdrop: #8a8a8c;
    --brick-red: #a8321f;
    --brick-dark: #7d2112;
    --brand-red: #d71920;
    --ink: #111111;
    --paper: #ffffff;
    --muted: #cfcfcf;
    --text-dark: #333333;
  }
  * { margin: 0; padding: 0; box-sizing: border-box; }
  html, body { width: 1200px; height: 908px; overflow: hidden; }
  body {
    background: var(--backdrop);
    font-family: "Open Sans", Arial, sans-serif;
    position: relative;
  }
  .card {
    position: absolute;
    top: 305px;
    width: 520px;
    height: 297px;
    border-radius: 16px;
    overflow: hidden;
  }
  .card-back { left: 60px; }
  .card-front { left: 620px; background: var(--paper); }

  .brick-field {
    position: absolute; inset: 0;
    background: radial-gradient(ellipse at 40% 30%, var(--brick-red), var(--brick-dark));
  }
  .back-brand {
    position: absolute; left: 0; right: 0; top: 126px;
    display: flex; align-items: center; justify-content: center; gap: 12px;
    font-family: "Oswald", Arial, sans-serif; font-weight: 600;
    font-size: 34px; letter-spacing: 1px; text-transform: uppercase;
    color: var(--paper);
  }
  .back-brand .mark-dot { width: 22px; height: 22px; border-radius: 50%; background: var(--paper); }

  .front-art { position: absolute; inset: 0; }
  .front-brand {
    position: absolute; left: 26px; top: 44px;
    display: flex; align-items: center; gap: 10px;
    font-family: "Oswald", Arial, sans-serif; font-weight: 600;
    font-size: 22px; line-height: 1.05; text-transform: uppercase;
    color: var(--brand-red);
  }
  .front-brand .mark-dot { width: 16px; height: 16px; border-radius: 50%; background: var(--brand-red); flex: none; }

  .contact-list {
    position: absolute; left: 330px; top: 28px;
    border-left: 1px solid var(--muted);
    padding-left: 12px;
    list-style: none;
    font-size: 9.5px; line-height: 1.45; color: var(--text-dark);
  }
  .contact-list li { display: flex; align-items: flex-start; gap: 6px; }
  .contact-list svg { width: 10px; height: 10px; flex: none; margin-top: 3px; }

  .person {
    position: absolute; left: 26px; top: 226px;
    display: flex; align-items: center; gap: 14px;
    color: var(--paper);
  }
  .person-name { font-size: 19px; font-weight: 400; }
  .person-title {
    border-left: 1px solid var(--paper);
    padding-left: 12px;
    font-size: 10.5px; line-height: 1.35;
  }
</style>
</head>
<body>

  <section class="card card-back">
    <div class="brick-field" role="img" aria-label="Red brick wall pattern background"></div>
    <div class="back-brand"><span class="mark-dot"></span>Brimstack Construction</div>
  </section>

  <section class="card card-front">
    <svg class="front-art" viewBox="0 0 520 297" width="520" height="297" aria-hidden="true">
      <path d="M0,178 C180,222 360,140 520,108 L520,122 C360,154 180,236 0,192 Z" fill="var(--brand-red)"/>
      <path d="M0,196 C180,240 360,158 520,126 L520,297 L0,297 Z" fill="var(--ink)"/>
      <path d="M0,170 C180,214 360,132 520,100" fill="none" stroke="var(--muted)" stroke-width="1.5"/>
    </svg>

    <div class="front-brand"><span class="mark-dot"></span><span>Brimstack<br>Construction</span></div>

    <ul class="contact-list">
      <li>
        <svg viewBox="0 0 10 10"><path d="M5 0.5a3.2 3.2 0 0 0-3.2 3.2C1.8 6.2 5 9.5 5 9.5s3.2-3.3 3.2-5.8A3.2 3.2 0 0 0 5 0.5z" fill="var(--brand-red)"/><circle cx="5" cy="3.7" r="1.2" fill="var(--paper)"/></svg>
        <span>7148 Orchard Lane, Unit 512<br>Myrtle Beach, SC 29614</span>
      </li>
      <li>
        <svg viewBox="0 0 10 10"><circle cx="5" cy="5" r="5" fill="var(--brand-red)"/><path d="M3.2 2.6l1 .9-.5.8c.4.8 1 1.4 1.9 1.9l.8-.5.9 1-.7.8C4.7 7.3 2.7 5.3 2.5 3.3z" fill="var(--paper)"/></svg>
        <span>843.555.0178 ext. 214</span>
      </li>
      <li>
        <svg viewBox="0 0 10 10"><circle cx="5" cy="5" r="5" fill="var(--brand-red)"/><rect x="2.4" y="3.2" width="5.2" height="3.6" fill="var(--paper)"/><path d="M2.4 3.2L5 5.2l2.6-2" fill="none" stroke="var(--brand-red)" stroke-width=".6"/></svg>
        <span>Karl@BrimstackLLC.example</span>
      </li>
      <li>
        <svg viewBox="0 0 10 10"><circle cx="5" cy="5" r="5" fill="var(--brand-red)"/><circle cx="5" cy="5" r="2.8" fill="none" stroke="var(--paper)" stroke-width=".6"/><path d="M2.2 5h5.6M5 2.2c-1.4 1.6-1.4 4 0 5.6M5 2.2c1.4 1.6 1.4 4 0 5.6" fill="none" stroke="var(--paper)" stroke-width=".5"/></svg>
        <span>www.BrimstackLLC.example</span>
      </li>
    </ul>

    <div class="person">
      <span class="person-name">Karl T. Wentworth</span>
      <span class="person-title">V.P., Operations &amp;<br>Sr. Project Manager</span>
    </div>
  </section>

</body>
</html>
```